Interior Stylist business card design needed

I need a business card for my new company in Sydney called "Pip Dunstane Designs". The business offers an interior styling and colour consultancy. My clients are generally not very design savvy (hence why they use me) and can range from being quite conservative to really wanting something "out there". They can be looking for a budget makeover or something more expensive / substantial. I'd like my business card design to be stylish (but not overly formal). I certainly don't want it to be conservative. I'd like it to stand out a bit! I don't really have any aversion to particular colours and I don't have a logo as such - my business name is really all I have.

Target Market(s)

As above - home owners, ranging from conservative to modern

Industry/Entity Type

Conservative

Contact Information for Business Card

Pip Dunstane Designs
Colour consultancy and interior styling
ph: 0417 382 605
email: pipdunstane@harvolink.net.au

Requirements
Should not have
• Old fashioned writing or motifs. No Times Roman font!!

```html
<!DOCTYPE html>
<html lang="en">
<head>
<meta charset="utf-8">
<title>Pip Dunstane Designs — Business Card</title>
<link rel="stylesheet" href="https://fonts.googleapis.com/css2?family=Josefin+Sans:wght@400&family=Roboto:wght@300&display=swap">
<style>
  :root {
    --stage: #2b2828;
    --card-dark: #0f0f10;
    --card-dark-sheen: #2a2830;
    --card-light: #eceae6;
    --ink-white: #ffffff;
    --ink-plum: #5b2a5e;
    --ink-grey: #6e6c6c;
    --ink-dark-grey: #8a8890;
  }
  * { box-sizing: border-box; margin: 0; padding: 0; }
  html, body {
    width: 1200px; height: 901px; overflow: hidden;
    background: var(--stage);
  }
  .stage {
    position: relative; width: 1200px; height: 901px;
    display: flex; align-items: center; justify-content: center; gap: 50px;
  }
  .card {
    position: relative; width: 525px; height: 300px;
    box-shadow: 0 10px 30px rgba(0,0,0,0.45);
  }
  .card--front {
    background: var(--card-dark);
    color: var(--ink-white);
    overflow: hidden;
  }
  .card__pattern {
    position: absolute; inset: 0;
    background: linear-gradient(150deg, var(--card-dark-sheen) 0%, var(--card-dark) 55%, #050505 100%);
  }
  .card--back { background: var(--card-light); }

  .wordmark {
    position: absolute; text-align: center;
    font-family: "Josefin Sans", sans-serif; font-weight: 400;
  }
  .wordmark__name {
    display: block; font-size: 34px; letter-spacing: 3px;
    text-transform: uppercase; line-height: 1;
  }
  .wordmark__tag {
    display: block; margin-top: 2px;
    font-family: "Roboto", sans-serif; font-weight: 300;
    font-size: 13px; letter-spacing: 1.5px; text-transform: uppercase;
  }
  .card--front .wordmark { left: 0; right: 0; top: 122px; }
  .card--front .wordmark__tag { color: var(--ink-dark-grey); }

  .card--back .wordmark { left: 0; right: 0; top: 88px; }
  .card--back .wordmark__name { color: var(--ink-plum); font-size: 30px; }
  .card--back .wordmark__tag { color: var(--ink-grey); }

  .contacts {
    position: absolute; left: 26px; right: 26px; bottom: 40px;
    display: flex; justify-content: space-between; align-items: center;
    list-style: none;
    font-family: "Roboto", sans-serif; font-weight: 300;
    font-size: 12.5px; color: var(--ink-grey);
  }
  .contacts__item { display: flex; align-items: center; gap: 6px; white-space: nowrap; }
  .contacts__icon { width: 12px; height: 12px; fill: var(--ink-plum); stroke: var(--ink-plum); }
</style>
</head>
<body>
<main class="stage">
  <section class="card card--front" aria-label="Business card front">
    <div class="card__pattern" role="img" aria-label="Dark card face with a repeating pattern of small glossy triangles"></div>
    <div class="wordmark">
      <span class="wordmark__name">Pip Dunstane</span>
      <span class="wordmark__tag">Designs</span>
    </div>
  </section>

  <section class="card card--back" aria-label="Business card back">
    <div class="wordmark">
      <span class="wordmark__name">Pip Dunstane</span>
      <span class="wordmark__tag">Designs</span>
    </div>
    <ul class="contacts">
      <li class="contacts__item">
        <svg class="contacts__icon" viewBox="0 0 12 12" aria-hidden="true"><path stroke="none" d="M1 4 Q6 0 11 4 L9 5 L8 3.5 L4 3.5 L3 5 Z M3 6 H9 L10 11 H2 Z"/></svg>
        0417 382 605
      </li>
      <li class="contacts__item">
        <svg class="contacts__icon" viewBox="0 0 12 12" aria-hidden="true"><rect x="1" y="3" width="10" height="7" stroke="none"/><path d="M1 3 L6 7 L11 3" fill="none" stroke="#eceae6" stroke-width="1"/></svg>
        pipdunstane@harvolink.net.au
      </li>
      <li class="contacts__item">
        <svg class="contacts__icon" viewBox="0 0 12 12" aria-hidden="true"><circle cx="7" cy="5" r="3.2" fill="none" stroke-width="1.4"/><line x1="4.8" y1="7.2" x2="1.5" y2="10.5" stroke-width="1.6"/></svg>
        www.pipdunstanedesigns.com.au
      </li>
    </ul>
  </section>
</main>
</body>
</html>
```